Harbor Crest Fleet Service Buisness card

We need to create a business card with the same theme you came up with for the truck. I have attached a picture of the truck for you to see. Also there is a picture of the logo as well as a sample business card that I really don't like.

Target Market(s)

Fleet service and heave equipment work

Industry/Entity Type

Fleet Service

Contact Information for Business Card

I have attached a sample card I want to make better. It has basic details on it.

Colors
0054AA
0677BA
7BADD7
CADEEF
E8F1F8
F0912C
F2A743
F7CA91
FBE8D2
FDF5EE

Requirements
Must have
• "Professional and clean, and I want to list some basic services. They include, "Mobile Hydraulics", Fleet Service, Computer diagnostics, "Roadside Service". I also want it to say "We come to you" and 24/7"
Nice to have
• Our Phone number is 1-888-512-7694

```html
<!DOCTYPE html>
<html lang="en">
<head>
<meta charset="utf-8">
<title>Harbor Crest Fleet Service – Business Card</title>
<link rel="stylesheet" href="https://fonts.googleapis.com/css2?family=Russo+One&family=Poppins:wght@500;600&display=swap">
<style>
  :root {
    --navy: #0f3f68;
    --orange: #f5b25b;
    --grey: #a7a7a7;
    --grey-soft: #d9d9d9;
    --white: #ffffff;
    --backdrop: #e9edf1;
  }
  * { box-sizing: border-box; margin: 0; padding: 0; }
  html, body { width: 1200px; height: 900px; overflow: hidden; background: var(--backdrop); }
  .stage {
    width: 1200px; height: 900px;
    display: flex; flex-direction: column; align-items: center; justify-content: center; gap: 40px;
  }
  .card {
    position: relative; width: 700px; height: 400px; border-radius: 26px; overflow: hidden;
    box-shadow: 0 8px 24px rgba(0,0,0,.18);
  }

  /* Front */
  .card-front { background: var(--navy); }
  .front-brand {
    position: absolute; left: 0; right: 0; top: 140px; text-align: center;
    font-family: "Russo One", sans-serif; font-weight: 400; color: var(--white); font-size: 40px; line-height: 1.1; letter-spacing: 1px;
  }
  .front-phone {
    position: absolute; left: 0; right: 0; top: 300px;
    display: flex; align-items: center; justify-content: center; gap: 10px;
    font-family: "Russo One", sans-serif; color: var(--white); font-size: 26px;
  }

  /* Back */
  .card-back { background: var(--white); }
  .back-brand {
    position: absolute; left: 40px; top: 48px; width: 320px;
    font-family: "Russo One", sans-serif; font-weight: 400; color: var(--navy); font-size: 34px; line-height: 1.05;
  }
  .services { position: absolute; left: 40px; top: 180px; list-style: none; }
  .service {
    height: 34px; margin-bottom: 7px; padding-left: 16px; border-radius: 0 10px 10px 10px;
    background: var(--navy); color: var(--white);
    font-family: "Russo One", sans-serif; font-size: 19px; line-height: 34px; letter-spacing: .5px;
    white-space: nowrap;
  }
  .service:nth-child(1) { width: 300px; }
  .service:nth-child(2) { width: 320px; }
  .service:nth-child(3) { width: 340px; }
  .service:nth-child(4) { width: 360px; }
  .usdot {
    position: absolute; left: 40px; top: 346px; width: 300px; height: 32px; padding-left: 16px;
    background: var(--grey); color: var(--white); border-radius: 10px 0 0 10px;
    font-family: "Russo One", sans-serif; font-size: 18px; line-height: 32px;
  }
  .contact { position: absolute; right: 36px; top: 34px; width: 340px; text-align: right; }
  .person-name { font-family: "Russo One", sans-serif; color: var(--navy); font-size: 26px; }
  .person-title { font-family: "Russo One", sans-serif; color: var(--orange); font-size: 17px; margin-top: 2px; }
  .phone-bar {
    display: flex; height: 40px; margin-top: 10px; border-radius: 10px; overflow: hidden;
  }
  .phone-bar .icon-cell { width: 64px; background: var(--orange); display: flex; align-items: center; justify-content: center; }
  .phone-bar .number {
    flex: 1; background: var(--navy); color: var(--white); text-align: center;
    font-family: "Russo One", sans-serif; font-size: 24px; line-height: 40px;
  }
  .contact-lines { list-style: none; margin-top: 12px; }
  .contact-line {
    display: flex; justify-content: flex-end; align-items: center; gap: 8px;
    font-family: "Poppins", sans-serif; font-weight: 500; color: var(--navy); font-size: 14.5px; line-height: 24px;
  }
  .contact-line .badge { width: 18px; height: 18px; border-radius: 4px; background: var(--orange); display: flex; align-items: center; justify-content: center; }
  .contact-line.plain { padding-right: 26px; }
  .tagline-band {
    position: absolute; right: 0; bottom: 0; width: 330px; height: 50px; background: var(--navy);
    color: var(--white); font-family: "Russo One", sans-serif; font-size: 18px; line-height: 50px; padding-left: 22px;
  }
  .always-open {
    position: absolute; right: 130px; bottom: 56px;
    font-family: "Russo One", sans-serif; font-size: 62px; line-height: 1; color: var(--navy);
  }
  .always-open .slash { color: var(--orange); }
  .stopwatch-placeholder {
    position: absolute; right: 36px; bottom: 62px; width: 80px; height: 56px; border-radius: 10px;
    background: linear-gradient(135deg, var(--grey-soft), var(--grey));
  }
</style>
</head>
<body>
<main class="stage">
  <section class="card card-front" aria-label="Business card front">
    <h1 class="front-brand">Harbor Crest<br>Fleet Service</h1>
    <p class="front-phone">
      <svg width="22" height="22" viewBox="0 0 24 24" aria-hidden="true"><path fill="#f5b25b" d="M6.6 10.8a15 15 0 0 0 6.6 6.6l2.2-2.2c.3-.3.7-.4 1-.2 1.1.4 2.3.6 3.6.6.6 0 1 .4 1 1V20c0 .6-.4 1-1 1A17 17 0 0 1 3 4c0-.6.4-1 1-1h3.5c.6 0 1 .4 1 1 0 1.3.2 2.5.6 3.6.1.3 0 .7-.2 1z"/></svg>
      1-888-512-7694
    </p>
  </section>

  <section class="card card-back" aria-label="Business card back">
    <h2 class="back-brand">Harbor Crest<br>Fleet Service</h2>

    <ul class="services">
      <li class="service">MOBILE HYDRAULICS</li>
      <li class="service">FLEET SERVICE</li>
      <li class="service">COMPUTER DIAGNOSTICS</li>
      <li class="service">ROADSIDE SERVICE</li>
    </ul>
    <p class="usdot">USDOT#2048137</p>

    <div class="contact">
      <p class="person-name">DANIEL MARSH</p>
      <p class="person-title">MANAGER</p>
      <div class="phone-bar">
        <span class="icon-cell">
          <svg width="22" height="22" viewBox="0 0 24 24" aria-hidden="true"><path fill="#0f3f68" d="M6.6 10.8a15 15 0 0 0 6.6 6.6l2.2-2.2c.3-.3.7-.4 1-.2 1.1.4 2.3.6 3.6.6.6 0 1 .4 1 1V20c0 .6-.4 1-1 1A17 17 0 0 1 3 4c0-.6.4-1 1-1h3.5c.6 0 1 .4 1 1 0 1.3.2 2.5.6 3.6.1.3 0 .7-.2 1z"/></svg>
        </span>
        <span class="number">1-888-512-7694</span>
      </div>
      <ul class="contact-lines">
        <li class="contact-line">daniel@harborcrestrentals.com
          <span class="badge"><svg width="12" height="10" viewBox="0 0 12 10" aria-hidden="true"><rect x=".5" y=".5" width="11" height="9" fill="none" stroke="#0f3f68"/><path d="M.5 .5 6 5.5 11.5 .5" fill="none" stroke="#0f3f68"/></svg></span></li>
        <li class="contact-line">www.harborcrestrentals.com
          <span class="badge"><svg width="12" height="12" viewBox="0 0 12 12" aria-hidden="true"><circle cx="6" cy="6" r="5" fill="none" stroke="#0f3f68"/><path d="M1 6h10M6 1c-3 3-3 7 0 10M6 1c3 3 3 7 0 10" fill="none" stroke="#0f3f68"/></svg></span></li>
        <li class="contact-line">4120 Palm Ridge Road
          <span class="badge"><svg width="10" height="12" viewBox="0 0 10 12" aria-hidden="true"><path d="M5 12S0 7 0 4.5a5 5 0 0 1 10 0C10 7 5 12 5 12z" fill="#0f3f68"/><circle cx="5" cy="4.5" r="1.8" fill="#f5b25b"/></svg></span></li>
        <li class="contact-line plain">Lakeview FL 33010</li>
      </ul>
    </div>

    <div class="stopwatch-placeholder" role="img" aria-label="Stopwatch illustration"></div>
    <p class="always-open">24<span class="slash">/</span>7</p>
    <p class="tagline-band">WE COME TO YOU AND</p>
  </section>
</main>
</body>
</html>
```